Game, Voice & Dedicated Server Company Needs a Business Card Design

We need a new business card design, centered around our new logo (PSD provided below).

Designs that we do like:
https://plomvaste.net/item/corporate-business-card/5382047?s_rank=31 (needs to be made more eye catching)

Our main areas of business are:
- Dedicated Servers
- Game Servers
- Voice Servers
- Mitigation Security Specialists

Industry/Entity Type

Business

Contact Information for Business Card

On the card: (and anything else you would suggest)
- Staff member name
- Staff member position in company
- Staff member phone number
- Staff member email
- Other / Staff member Skype
- Website link

Colors
9bcb3c
abd036

Requirements
Must have
• Design of Card:
• - Green (same green as the logo)
• - Business / Corporate design
• - Something a little different / abstract that shouts premium

```html
<!DOCTYPE html>
<html lang="en">
<head>
<meta charset="utf-8">
<title>Tidewell Hosting – Business Card</title>
<link href="https://fonts.googleapis.com/css2?family=Roboto:wght@400;500;700;900&display=swap" rel="stylesheet">
<style>
  :root {
    --backdrop: #2b2624;
    --card: #1c1c1d;
    --card-edge: #141414;
    --green: #9bcb3c;
    --green-alt: #abd036;
    --text: #e9e9e9;
    --muted: #9a9a9a;
    --emboss: #6d6d6f;
  }
  * { margin: 0; padding: 0; box-sizing: border-box; }
  html, body { width: 1200px; height: 787px; overflow: hidden; }
  body {
    background: var(--backdrop);
    font-family: 'Roboto', Arial, sans-serif;
    position: relative;
  }
  .card {
    position: absolute;
    width: 540px;
    height: 310px;
    background: var(--card);
    border-radius: 4px;
    box-shadow: 0 10px 28px rgba(0,0,0,.45);
    overflow: hidden;
  }
  .card--front { left: 40px; top: 110px; }
  .card--back { left: 620px; top: 367px; }

  /* front */
  .front-brand {
    position: absolute; left: 70px; top: 78px;
    display: flex; align-items: center; gap: 16px;
  }
  .brand-mark { width: 44px; height: 44px; background: var(--emboss); }
  .front-brand .brand-name {
    color: var(--emboss); font-weight: 900; font-size: 34px;
    line-height: .95; letter-spacing: -0.5px; text-transform: uppercase;
  }
  .services {
    position: absolute; left: 70px; top: 190px;
    color: var(--text); font-size: 15px; line-height: 1.45; list-style: none;
  }
  .services .dot {
    display: inline-block; width: 6px; height: 6px; border-radius: 50%;
    background: var(--green); margin: 0 6px 2px; vertical-align: middle;
  }

  /* back */
  .staff { position: absolute; left: 34px; top: 96px; }
  .staff-name { color: var(--green); font-weight: 500; font-size: 19px; }
  .staff-role { color: var(--muted); font-size: 12px; margin-top: 2px; }
  .contact-list { list-style: none; margin-top: 12px; }
  .contact-list li {
    color: var(--text); font-size: 15px; display: flex; align-items: center;
    gap: 8px; line-height: 1.55;
  }
  .contact-list svg { width: 13px; height: 13px; fill: var(--green); }
  .back-brand {
    position: absolute; right: 30px; top: 104px;
    display: flex; align-items: center; gap: 12px;
  }
  .back-brand .brand-mark { width: 40px; height: 40px; background: var(--green); }
  .back-brand .brand-name {
    color: var(--green); font-weight: 900; font-size: 30px;
    line-height: .95; letter-spacing: -0.5px; text-transform: uppercase;
  }
  .divider {
    position: absolute; left: 34px; right: 30px; top: 210px;
    height: 1px; background: var(--text);
  }
  .web-list {
    position: absolute; right: 30px; top: 222px;
    list-style: none; text-align: right;
  }
  .web-list li {
    color: var(--text); font-size: 15px; line-height: 1.55;
    display: flex; justify-content: flex-end; align-items: center; gap: 8px;
  }
  .web-list .badge {
    width: 13px; height: 13px; border-radius: 50%; background: var(--green);
  }
</style>
</head>
<body>
  <section class="card card--front" aria-label="Card front">
    <div class="front-brand">
      <span class="brand-mark"></span>
      <span class="brand-name">Tidewell<br>Hosting</span>
    </div>
    <ul class="services">
      <li>Dedicated Servers<span class="dot"></span>Game Servers</li>
      <li>Voice Servers<span class="dot"></span>Business relations</li>
    </ul>
  </section>

  <section class="card card--back" aria-label="Card back">
    <div class="staff">
      <p class="staff-name">Aron Vale</p>
      <p class="staff-role">CEO/Founder</p>
      <ul class="contact-list">
        <li>
          <svg viewBox="0 0 16 16" aria-hidden="true"><path d="M3 1h3l1.5 4-2 1.3a9 9 0 0 0 4.2 4.2L11 8.5l4 1.5v3a2 2 0 0 1-2 2A13 13 0 0 1 1 3a2 2 0 0 1 2-2z"/></svg>
          555 214 0973
        </li>
        <li>
          <svg viewBox="0 0 16 16" aria-hidden="true"><path d="M1 3h14v10H1z M1 3l7 6 7-6" stroke="#1c1c1d" stroke-width="1.2"/></svg>
          name@tidewell.com
        </li>
      </ul>
    </div>
    <div class="back-brand">
      <span class="brand-mark"></span>
      <span class="brand-name">Tidewell<br>Hosting</span>
    </div>
    <div class="divider"></div>
    <ul class="web-list">
      <li>www.tidewell.com</li>
      <li>tidewell.com <span class="badge"></span></li>
      <li>tidewell.com <span class="badge"></span></li>
    </ul>
  </section>
</body>
</html>
```